I want to create a postcard we can use as a promotional offer. We may send out to prospects or give to people at an event to get them in front of us and start to understand their business more with the hope of engaging them as clients eventually.
The offer is a Complimentary "Venture Spark Kit". (valued at $875)
The kit includes:
Fiscal Horizon Audit
45 minute Business Discovery Meeting
6 point Diagnostic Report
3 Recommendations for your Business

The headline and there look and feel we would like the design to be focused upon is "Analyze. Boost. Grow."
Include an Image(s) as you feel appropriate.
I'm thinking Headline/Mian Branding and Picture on the Front, then Offer and details of Kit and Logos etc on the Back.

Include 2 logos as we are part of a joint operation, Meridale Accountants & Trovenly.

Call to action to Phone 0255501872 or email hello@trovenly.com.au

Logo's uploaded, committed payment, increased deadline.

Target Market(s)

Small to Medium Business

Industry/Entity Type

Business

Requirements
Must have
• Logos in Colour on Back with rest of Detail.
Front to be all about the key message "Analyze. Boost. Grow." select pic to represent.
Must create cut through and intrigue to make the holder tunr the card and read.

```html
<!DOCTYPE html>
<html lang="en">
<head>
<meta charset="utf-8">
<title>Venture Spark Kit Postcard</title>
<link href="https://fonts.googleapis.com/css2?family=PT+Sans:ital,wght@0,400;0,700;1,400;1,700&display=swap" rel="stylesheet">
<style>
  :root{
    --green:#5db531;
    --green-dark:#3f9a22;
    --navy:#1d4f7a;
    --teal:#20608c;
    --sky:#cfe6f7;
    --ink:#1f2a36;
    --page:#eeeeee;
    --white:#ffffff;
    --band:#d7ebf8;
  }
  *{box-sizing:border-box;margin:0;padding:0}
  html,body{width:1181px;height:1200px;overflow:hidden}
  body{background:var(--page);font-family:"PT Sans",Arial,sans-serif;position:relative;color:var(--ink)}

  .card{position:absolute;width:700px;height:543px;background:var(--white);overflow:hidden;box-shadow:0 4px 14px rgba(0,0,0,.18)}
  .card--front{left:40px;top:33px}
  .card--back{left:441px;top:622px;background:linear-gradient(180deg,var(--sky) 0%,#eef6fc 40%,var(--white) 70%)}

  /* front */
  .hero-photo{position:absolute;left:0;top:0;width:700px;height:430px;
    background:linear-gradient(180deg,#a9d3f0 0%,#dcecf6 45%,#b9d7a8 62%,#6fae3a 80%,#4f8f25 100%)}
  .hero-hands{position:absolute;left:0;top:40px;width:440px;height:320px;border-radius:0 60% 50% 0;
    background:radial-gradient(ellipse at 60% 55%,rgba(214,160,120,.9) 0%,rgba(196,140,100,.6) 40%,rgba(120,150,90,0) 75%)}
  .headline{position:absolute;right:34px;top:42px;text-align:right;font-weight:700;font-style:italic;font-size:52px;line-height:1.12;letter-spacing:-.5px}
  .headline .g{color:var(--green)}
  .headline .b{color:var(--teal)}
  .swoosh{position:absolute;left:0;top:330px;width:700px;height:213px}
  .pillars{position:absolute;left:340px;top:325px;width:340px;height:120px}
  .pillar{position:absolute;width:76px;height:76px;border-radius:50%;border:3px solid var(--white);display:flex;flex-direction:column;align-items:center;justify-content:center;color:var(--white);font-size:10px;box-shadow:0 2px 4px rgba(0,0,0,.25)}
  .pillar--blue{background:var(--navy)}
  .pillar--green{background:var(--green)}
  .pillar svg{width:34px;height:30px;margin-bottom:3px}
  .brands{position:absolute;left:120px;top:440px;display:flex;align-items:center;gap:28px}
  .brand{font-weight:700;font-size:30px;line-height:1;white-space:nowrap}
  .brand--meridale{color:var(--navy)}
  .brand--trovenly{color:var(--green)}
  .brand-divider{width:2px;height:56px;background:var(--navy)}
  .contact-bar{position:absolute;left:34px;top:508px;width:642px;height:30px;background:linear-gradient(90deg,rgba(215,235,248,0),var(--band) 15%,var(--band) 85%,rgba(215,235,248,0));display:flex;align-items:center;justify-content:center;gap:34px}
  .contact{display:flex;align-items:center;gap:8px;font-weight:700;font-style:italic;font-size:25px;color:var(--navy);white-space:nowrap}
  .contact svg{width:28px;height:22px}

  /* back */
  .stamp{position:absolute;left:14px;top:16px;width:100px;height:62px;border:2px solid var(--teal);border-radius:50%;transform:rotate(-16deg);display:flex;align-items:center;justify-content:center;color:var(--teal);font-weight:700;font-size:9px;letter-spacing:0;white-space:nowrap}
  .kit-title{position:absolute;left:120px;top:22px;font-weight:700;font-style:italic;font-size:25px;color:var(--green);white-space:nowrap}
  .kit-list{position:absolute;left:96px;top:58px;width:250px;list-style:none}
  .kit-item{position:relative;height:48px}
  .kit-bar{position:absolute;left:40px;top:6px;width:210px;height:22px;background:var(--teal);border-radius:0 4px 4px 0;color:var(--white);font-weight:700;font-size:11.5px;line-height:22px;padding-left:20px;white-space:nowrap}
  .kit-num{position:absolute;left:0;top:-4px;width:48px;height:48px;border-radius:50%;background:var(--white);display:flex;flex-direction:column;align-items:center;justify-content:center;color:var(--green);font-weight:700;font-size:29px;line-height:.9;box-shadow:0 1px 3px rgba(0,0,0,.15)}
  .kit-num small{font-size:9px;color:var(--navy)}
  .plant-photo{position:absolute;left:20px;top:112px;width:70px;height:178px;border-radius:40% 40% 8px 8px;background:linear-gradient(180deg,#7cc04a 0%,#4e8f2c 70%,#9a9a9a 78%,#cfcfcf 100%)}
  .offer-badge{position:absolute;left:196px;top:234px;width:68px;height:68px}
  .offer-badge span{position:absolute;inset:0;display:flex;flex-direction:column;align-items:center;justify-content:center;color:var(--white);font-weight:700;font-size:13px;line-height:1}
  .offer-badge small{font-size:6.5px;margin-top:2px}
  .seedling-photo{position:absolute;left:360px;top:28px;width:140px;height:96px;border-radius:30% 50% 40% 30%;background:radial-gradient(ellipse at 40% 60%,#6b4a2e 0%,#d6a37a 35%,rgba(230,200,170,.6) 60%,rgba(230,240,250,0) 80%)}
  .back-swoosh{position:absolute;left:0;top:290px;width:380px;height:40px}
  .cta{position:absolute;left:20px;top:322px;width:330px;text-align:center;font-style:italic;font-weight:700;color:var(--green)}
  .cta-lead{font-size:11px;color:var(--green)}
  .cta-lead b{color:var(--navy)}
  .cta-title{font-size:24px;line-height:1.1}
  .back-brands{position:absolute;left:38px;top:372px;display:flex;align-items:center;gap:16px}
  .back-brands .brand{font-size:21px}
  .back-brands .brand-divider{height:40px}
  .back-contact{position:absolute;left:20px;top:432px;width:330px;height:22px;background:linear-gradient(90deg,rgba(215,235,248,0),var(--band) 15%,var(--band) 85%,rgba(215,235,248,0));display:flex;align-items:center;justify-content:center;gap:14px}
  .back-contact .contact{font-size:15px;gap:5px}
  .back-contact svg{width:16px;height:13px}
  .mail-label{position:absolute;font-family:Arial,Helvetica,sans-serif;font-size:16px;color:#000;text-align:center;white-space:nowrap}
  .mail-label--postage{left:515px;top:28px}
  .mail-label--address{left:440px;top:232px}
  .mail-label--barcode{left:400px;top:440px}
</style>
</head>
<body>

<section class="card card--front" aria-label="Postcard front">
  <div class="hero-photo" role="img" aria-label="Cupped hands holding a small bonsai tree in front of a blue sky, lake and green meadow"></div>
  <div class="hero-hands" aria-hidden="true"></div>
  <h1 class="headline"><span class="g">Analyze.</span><br><span class="b">Boost.</span><br><span class="g">Grow.</span></h1>

  <svg class="swoosh" viewBox="0 0 700 213" preserveAspectRatio="none" aria-hidden="true">
    <path d="M0 95 Q300 -10 700 40 L700 213 L0 213 Z" fill="var(--white)"/>
    <path d="M0 80 Q300 -22 700 26 L700 38 Q300 -8 0 96 Z" fill="var(--navy)"/>
  </svg>

  <div class="pillars">
    <div class="pillar pillar--blue" style="left:0;top:0">
      <svg viewBox="0 0 34 30"><rect x="4" y="16" width="4" height="10" fill="#fff"/><rect x="11" y="12" width="4" height="14" fill="#fff"/><path d="M6 14 L14 22 L31 3" stroke="var(--green)" stroke-width="4" fill="none"/></svg>
      Performance
    </div>
    <div class="pillar pillar--green" style="left:85px;top:-8px">
      <svg viewBox="0 0 34 30"><circle cx="17" cy="10" r="8" fill="#fff"/><rect x="15" y="16" width="4" height="12" fill="#fff"/></svg>
      Wealth
    </div>
    <div class="pillar pillar--blue" style="left:170px;top:0">
      <svg viewBox="0 0 34 30"><circle cx="12" cy="7" r="4" fill="#fff"/><circle cx="23" cy="7" r="4" fill="#fff"/><path d="M6 28 L10 13 L14 13 L18 28 Z M17 28 L21 13 L25 13 L29 28 Z" fill="#fff"/></svg>
      Lifestyle
    </div>
    <div class="pillar pillar--green" style="left:250px;top:18px">
      <svg viewBox="0 0 34 30"><circle cx="17" cy="12" r="9" fill="#fff"/><rect x="13" y="21" width="8" height="6" fill="#fff"/></svg>
      Dreams
    </div>
  </div>

  <div class="brands">
    <span class="brand brand--meridale">Meridale Accountants</span>
    <span class="brand-divider"></span>
    <span class="brand brand--trovenly">Trovenly</span>
  </div>

  <div class="contact-bar">
    <span class="contact"><svg viewBox="0 0 28 22"><path d="M2 8 Q14 -2 26 8 L22 11 L19 8 Q14 5 9 8 L6 11 Z" fill="var(--green)"/><rect x="7" y="11" width="14" height="9" rx="2" fill="var(--green)"/></svg>0255501872</span>
    <span class="contact"><svg viewBox="0 0 28 22"><rect x="1" y="3" width="26" height="17" rx="2" fill="var(--green)"/><path d="M2 4 L14 13 L26 4" stroke="#fff" stroke-width="2" fill="none"/></svg>hello@trovenly.com.au</span>
  </div>
</section>

<section class="card card--back" aria-label="Postcard back">
  <div class="stamp">COMPLIMENTARY</div>
  <h2 class="kit-title">Venture Spark Kit</h2>

  <div class="plant-photo" role="img" aria-label="Potted topiary plant shaped like a dollar sign"></div>

  <ol class="kit-list">
    <li class="kit-item"><span class="kit-bar">Business Discovery Meeting</span><span class="kit-num">45<small>minutes</small></span></li>
    <li class="kit-item"><span class="kit-bar">Diagnostic Report</span><span class="kit-num">6<small>point</small></span></li>
    <li class="kit-item"><span class="kit-bar">Recommendations for your Business</span><span class="kit-num">3</span></li>
    <li class="kit-item"><span class="kit-bar">Fiscal Horizon Audit</span><span class="kit-num">1</span></li>
  </ol>

  <div class="offer-badge">
    <svg viewBox="0 0 74 74" width="68" height="68" aria-hidden="true">
      <polygon points="37,1 43,10 53,4 55,15 66,13 63,24 73,28 65,37 73,46 63,50 66,61 55,59 53,70 43,64 37,73 31,64 21,70 19,59 8,61 11,50 1,46 9,37 1,28 11,24 8,13 19,15 21,4 31,10" fill="var(--green)"/>
      <circle cx="37" cy="37" r="26" fill="var(--teal)"/>
    </svg>
    <span>FREE<br>OFFER<small>Valued At $875</small></span>
  </div>

  <div class="seedling-photo" role="img" aria-label="Open hand holding soil with a young green seedling"></div>

  <svg class="back-swoosh" viewBox="0 0 380 40" preserveAspectRatio="none" aria-hidden="true">
    <path d="M0 30 Q180 -4 380 14 L380 20 Q180 4 0 36 Z" fill="var(--navy)"/>
  </svg>

  <div class="cta">
    <p class="cta-lead">Take your <b>Business</b> in a <b>New Direction</b> and request your</p>
    <p class="cta-title">Venture Spark Kit</p>
  </div>

  <div class="back-brands">
    <span class="brand brand--meridale">Meridale Accountants</span>
    <span class="brand-divider"></span>
    <span class="brand brand--trovenly">Trovenly</span>
  </div>

  <div class="back-contact">
    <span class="contact"><svg viewBox="0 0 28 22"><path d="M2 8 Q14 -2 26 8 L22 11 L19 8 Q14 5 9 8 L6 11 Z" fill="var(--green)"/><rect x="7" y="11" width="14" height="9" rx="2" fill="var(--green)"/></svg>0255501872</span>
    <span class="contact"><svg viewBox="0 0 28 22"><rect x="1" y="3" width="26" height="17" rx="2" fill="var(--green)"/><path d="M2 4 L14 13 L26 4" stroke="#fff" stroke-width="2" fill="none"/></svg>hello@trovenly.com.au</span>
  </div>

  <p class="mail-label mail-label--postage">Postage<br>Area</p>
  <p class="mail-label mail-label--address">Address Area</p>
  <p class="mail-label mail-label--barcode">Barcode Area</p>
</section>

</body>
</html>
```